Business Card Design - Photographer

I am a landscape photographer and I require a business card design. 

I require two designs:
1)  a double sided business card
 and
b)  a single sided business card 

The single sided design can either be the same as the double sided (with just one side having all the information)....or it can be an entire new design. Its up to you.

My corporate colours are (CMYK):

Blue   69, 32, 0, 0
Grey  72,  64,  47,  31
Green  32,  2,  91,  0
Yellow   0, 19, 92, 0
Orange  0, 39, 75, 0

Colour space in final file should be in CMYK.

The details that need to be included on the card:

- Use the provided Logo
- Name: Lukas Wendrovski
- Email:   sales@vistaplume.com.au
- Website:    vistaplume.com.au
- Twitter:    chirpline.com/vistaplume
- Facebook:   friendhub.com/vistaplume
- Mobile  0415 309 662

Please use the attached template to design the logo to the specified size, including the marked bleed lines. I have also attached my logo in PNG (transparent background) and ai format for you to use.

The final file should be:
- Photoshop version with layers so I can edit the name/text etc. All non vector files should be high resolution at 1039 x 697 pixels at 300 dpi.

I also require a file as:
- Vector based PDF

Anyway questions please contact me.

Thank you

Industry/Entity Type

Landscape

Logo styles of interest
Pictorial/Combination Logo
Abstract Logo
Wordmark Logo
Lettermark Logo
Requirements
Must have
• The details that need to be included on the card:

- Use the provided Logo
- Name: Lukas Wendrovski
- Email: sales@vistaplume.com.au
- Website: vistaplume.com.au
- Twitter: chirpline.com/vistaplume
- Facebook: friendhub.com/vistaplume
- Mobile 0415 309 662

```html
<!DOCTYPE html>
<html lang="en">
<head>
<meta charset="utf-8">
<title>Vista Plume — Business Cards</title>
<link href="https://fonts.googleapis.com/css2?family=Cinzel:wght@400;500&family=Share+Tech+Mono&display=swap" rel="stylesheet">
<style>
  :root {
    --backdrop: #e6e7ea;
    --navy-light: #41465e;
    --navy-dark: #22253a;
    --ink: #3a3d52;
    --paper: #ffffff;
    --paper-shade: #eef0f2;
    --blue: #3b95d5;
    --yellow: #f7c418;
    --text-dark: #26282f;
  }
  * { box-sizing: border-box; margin: 0; padding: 0; }
  html, body { width: 1200px; height: 840px; overflow: hidden; background: var(--backdrop); }
  .canvas {
    width: 1200px; height: 840px;
    display: flex; align-items: center; justify-content: center; gap: 40px;
  }
  .card {
    width: 560px; height: 376px; position: relative; overflow: hidden;
    box-shadow: 0 6px 18px rgba(0,0,0,.18);
  }
  /* Front */
  .card--front {
    background: radial-gradient(ellipse at 50% 30%, var(--navy-light), var(--navy-dark) 75%);
    color: var(--paper);
    display: flex; flex-direction: column; align-items: center;
  }
  .brand-mark { border-radius: 50%; display: block; }
  .card--front .brand-mark {
    width: 74px; height: 74px; background: var(--paper); margin-top: 70px;
  }
  .wordmark {
    font-family: "Cinzel", serif; font-weight: 500; letter-spacing: 1px;
    text-transform: uppercase; white-space: nowrap;
  }
  .card--front .wordmark {
    font-size: 36px; margin-top: 26px; padding: 0 6px 4px;
    border-bottom: 2px solid var(--paper);
  }
  .tagline {
    font-family: "Cinzel", serif; font-size: 13px; letter-spacing: 2.5px;
    margin-top: 8px; text-transform: uppercase;
  }
  .front-web {
    font-family: "Share Tech Mono", monospace; font-size: 16px;
    color: var(--yellow); margin-top: 38px; letter-spacing: .5px;
  }
  /* Back */
  .card--back {
    background: linear-gradient(160deg, var(--paper) 40%, var(--paper-shade));
    color: var(--text-dark);
  }
  .back-brand { position: absolute; left: 40px; top: 34px; display: flex; flex-direction: column; align-items: center; }
  .card--back .brand-mark { width: 60px; height: 60px; background: var(--ink); }
  .card--back .wordmark {
    color: var(--ink); font-size: 27px; margin-top: 12px; padding: 0 4px 3px;
    border-bottom: 1.5px solid var(--ink);
  }
  .holder { position: absolute; right: 40px; top: 134px; text-align: right; font-family: "Share Tech Mono", monospace; white-space: nowrap; }
  .holder__name { color: var(--blue); font-size: 25px; font-weight: 700; letter-spacing: .5px; }
  .holder__role { font-size: 15px; margin-top: 2px; }
  .holder-band { position: absolute; right: 0; top: 128px; width: 26px; height: 56px; background: var(--ink); }
  .contacts {
    position: absolute; left: 40px; bottom: 30px; list-style: none;
    font-family: "Share Tech Mono", monospace; font-size: 15px; line-height: 25px;
  }
  .contacts li { display: flex; align-items: center; gap: 10px; white-space: nowrap; }
  .contacts svg { width: 15px; height: 15px; fill: var(--blue); flex: none; }
</style>
</head>
<body>
<main class="canvas">
  <section class="card card--front" aria-label="Card front">
    <span class="brand-mark"></span>
    <h1 class="wordmark">Vista Plume</h1>
    <p class="tagline">Fine Art Photography</p>
    <p class="front-web">www.vistaplume.com.au</p>
  </section>

  <section class="card card--back" aria-label="Card back">
    <div class="back-brand">
      <span class="brand-mark"></span>
      <h2 class="wordmark">Vista Plume</h2>
    </div>
    <div class="holder">
      <p class="holder__name">Lukas Wendrovski</p>
      <p class="holder__role">Art Photography</p>
    </div>
    <span class="holder-band"></span>
    <ul class="contacts">
      <li><svg viewBox="0 0 16 16"><rect x="4" y="1" width="8" height="14" rx="1.5"/><rect x="5.5" y="3" width="5" height="7" fill="#fff"/></svg>0415-309-662</li>
      <li><svg viewBox="0 0 16 16"><rect x="1" y="3" width="14" height="10" rx="1"/><path d="M1.5 3.8 8 9l6.5-5.2" stroke="#fff" stroke-width="1.4" fill="none"/></svg>sales@vistaplume.com.au</li>
      <li><svg viewBox="0 0 16 16"><circle cx="8" cy="8" r="7"/><path d="M1 8h14M8 1c-3 3.5-3 10.5 0 14M8 1c3 3.5 3 10.5 0 14" stroke="#fff" stroke-width="1" fill="none"/></svg>www.vistaplume.com.au</li>
      <li><svg viewBox="0 0 16 16"><circle cx="8" cy="8" r="6.5"/></svg>chirpline.com/vistaplume</li>
      <li><svg viewBox="0 0 16 16"><rect x="1.5" y="1.5" width="13" height="13" rx="1"/></svg>friendhub.com/vistaplume</li>
    </ul>
  </section>
</main>
</body>
</html>
```